Flyer für Alltagsbegleitung
Zielgruppe
Firma: Tageshilfe am Fluss
Meine Zielgruppe sind alle Menschen, die im Alltag, Hilfe benötigen.
Aufgabenstellung
Der Flyer soll modern und und ansprechend aussehen. Es soll vermerkt sein, das ich als annerkannte Kraft, Entlastungsleistung nach

```html
<!DOCTYPE html>
<html lang="de">
<head>
<meta charset="utf-8">
<title>Tageshilfe am Fluss – Flyer</title>
<link rel="stylesheet" href="https://fonts.googleapis.com/css2?family=Anton&family=Poppins:wght@400;500;600;700;800&display=swap">
<style>
  :root{
    --stage:#d9d9d9;
    --paper:#f3f0ec;
    --slate:#566c85;
    --slate-dark:#4b5f77;
    --ink:#4a5568;
    --red:#c9343b;
    --white:#ffffff;
    --photo-a:#c9a98c;
    --photo-b:#8a6a55;
  }
  *{box-sizing:border-box;margin:0;padding:0}
  html,body{width:1200px;height:750px;overflow:hidden}
  body{background:var(--stage);font-family:"Poppins",sans-serif;color:var(--ink);position:relative}
  .flyer{position:absolute;top:64px;width:292px;height:622px;background:var(--paper);overflow:hidden;box-shadow:0 6px 18px rgba(0,0,0,.18)}
  .flyer--offer{left:250px}
  .flyer--cover{left:658px}
  .display{font-family:"Anton",sans-serif;color:var(--slate);text-transform:uppercase;line-height:1;letter-spacing:-.5px}

  /* Offer side */
  .offer-title{font-size:27px;text-align:center;margin-top:26px}
  .offer-band{background:var(--slate);color:var(--white);font-family:"Anton",sans-serif;font-size:25px;text-align:center;padding:8px 0 10px;margin:2px 8px 0;border-radius:10px;letter-spacing:-.5px}
  .intro{font-size:9px;line-height:1.45;text-align:center;padding:12px 14px 0}
  .services{list-style:none;background:var(--slate);color:var(--white);margin:16px 10px 0;border-radius:14px;padding:14px 14px 18px}
  .services li{font-size:11px;padding:5px 0;display:flex;align-items:center;gap:5px;justify-content:center}
  .services strong{font-weight:800}
  .services svg{width:12px;height:12px;flex:none}
  .badge{position:relative;width:64px;height:60px;margin:-14px auto 0;text-align:center;color:var(--white)}
  .badge svg{position:absolute;inset:0;width:100%;height:100%}
  .badge span{position:relative;display:block;font-size:6.5px;line-height:1.15;padding-top:15px}
  .badge b{font-size:8px;font-weight:800}
  .claim{font-size:9px;line-height:1.45;text-align:center;padding:14px 12px 0}
  .claim strong{font-weight:800}
  .address{background:var(--slate);color:var(--white);text-align:center;margin:20px 8px 0;border-radius:12px;padding:8px 0}
  .address .name{font-weight:700;font-size:12px}
  .address .street{font-size:12px}
  .heart-red{color:var(--red)}
  .follow{text-align:center;font-weight:800;color:var(--slate);font-size:10.5px;margin-top:9px}
  .handle{display:flex;align-items:center;justify-content:center;gap:5px;font-size:9px;margin-top:3px}
  .dot{width:14px;height:14px;border-radius:50%;background:var(--red)}

  /* Cover side */
  .cover-title{text-align:center;margin-top:18px}
  .cover-title .small{font-size:34px;display:block}
  .cover-title .large{font-size:34px;display:block;margin-top:4px}
  .brand-row{display:flex;align-items:center;justify-content:center;gap:12px;margin-top:10px;height:84px}
  .brand{display:flex;align-items:center;gap:5px;font-weight:600;font-size:12px;color:var(--slate-dark);width:110px;line-height:1.2}
  .brand .mark{width:12px;height:12px;border-radius:50%;background:var(--red);flex:none}
  .photo{background:linear-gradient(135deg,var(--photo-a),var(--photo-b))}
  .photo--hands{width:90px;height:82px;border-radius:8px}
  .cover-sub{font-family:"Anton",sans-serif;color:var(--slate);font-size:27px;text-align:center;margin-top:6px;letter-spacing:-.5px}
  .tagline{font-size:9.5px;text-align:center;margin-top:6px}
  .gallery{background:var(--slate);margin-top:14px;border-radius:12px;padding:11px 14px;display:flex;gap:12px}
  .photo--scene{flex:1;height:80px;border:3px solid var(--white);border-radius:6px}
  .body-copy{font-size:8.6px;line-height:1.45;text-align:center;padding:20px 8px 0}
  .body-copy p+p{margin-top:10px}
  .cta{background:var(--slate);color:var(--white);text-align:center;border-radius:12px;margin-top:30px;padding:6px 0 8px}
  .cta .label{font-weight:700;font-size:12px;letter-spacing:.3px}
  .cta .phone{font-size:16px;display:flex;align-items:center;justify-content:center;gap:6px}
  .cta svg{width:13px;height:13px}
  .note{font-weight:700;font-size:8.5px;text-align:center;color:var(--slate-dark);margin-top:12px;line-height:1.4}
</style>
</head>
<body>
  <article class="flyer flyer--offer">
    <h2 class="display offer-title">Mein Angebot für Sie -</h2>
    <div class="offer-band">MEHR ALS NUR UNTERSTÜTZUNG</div>
    <p class="intro">Mein Ziel ist es,<br>Ihnen und Ihren Angehörigen Freiräume zu schaffen und gleichzeitig die Selbstständigkeit und Lebensfreude der Senioren zu fördern.<br>Ich passe meine Unterstützung individuell an Ihre Bedürfnisse an, immer mit Respekt und Verständnis.</p>
    <ul class="services">
      <li><svg viewBox="0 0 24 24"><path d="M12 21s-8-5.5-8-11a4.5 4.5 0 0 1 8-2.8A4.5 4.5 0 0 1 20 10c0 5.5-8 11-8 11z" fill="none" stroke="#fff" stroke-width="2"/></svg><span><strong>Unterstützung</strong> im Haushalt</span></li>
      <li><svg viewBox="0 0 24 24"><path d="M12 21s-8-5.5-8-11a4.5 4.5 0 0 1 8-2.8A4.5 4.5 0 0 1 20 10c0 5.5-8 11-8 11z" fill="none" stroke="#fff" stroke-width="2"/></svg><span><strong>Begleitung</strong> außer Haus</span></li>
      <li><svg viewBox="0 0 24 24"><path d="M12 21s-8-5.5-8-11a4.5 4.5 0 0 1 8-2.8A4.5 4.5 0 0 1 20 10c0 5.5-8 11-8 11z" fill="none" stroke="#fff" stroke-width="2"/></svg><span>Aktivierende <strong>Freizeitgestaltung</strong></span></li>
      <li><svg viewBox="0 0 24 24"><path d="M12 21s-8-5.5-8-11a4.5 4.5 0 0 1 8-2.8A4.5 4.5 0 0 1 20 10c0 5.5-8 11-8 11z" fill="none" stroke="#fff" stroke-width="2"/></svg><span><strong>Entlastung</strong> für pflegende Angehörige</span></li>
      <li><svg viewBox="0 0 24 24"><path d="M12 21s-8-5.5-8-11a4.5 4.5 0 0 1 8-2.8A4.5 4.5 0 0 1 20 10c0 5.5-8 11-8 11z" fill="none" stroke="#fff" stroke-width="2"/></svg><span><strong>Organisation</strong> und <strong>Vermittlung</strong></span></li>
    </ul>
    <div class="badge">
      <svg viewBox="0 0 24 24"><path d="M12 22S2 15 2 8.5A5 5 0 0 1 12 6a5 5 0 0 1 10 2.5C22 15 12 22 12 22z" fill="var(--red)"/></svg>
      <span>JETZT<br><b>131 EURO</b><br>sichern!</span>
    </div>
    <p class="claim">Jeder Pflegebedürftige mit einem Pflegegrad hat <strong>Anspruch</strong> auf einen <strong>monatlichen Entlastungsbetrag</strong> in Höhe von <strong>131 Euro</strong>. Dieser Betrag kann für Angebote zur Unterstützung im Alltag verwendet werden, wie ich sie anbiete.</p>
    <div class="address">
      <div class="name">Ihre Lena Vogt</div>
      <div class="street">Musterstraße 00 <span class="heart-red">♥</span> 01234 Musterstadt</div>
    </div>
    <p class="follow">JETZT folgen &amp; nichts mehr verpassen!</p>
    <p class="handle"><span class="dot"></span>@lenavogt_tageshilfe</p>
  </article>

  <article class="flyer flyer--cover">
    <h1 class="display cover-title"><span class="small">Ihre</span><span class="large">Alltagsbegleitung</span></h1>
    <div class="brand-row">
      <div class="brand"><span class="mark"></span>Tageshilfe am Fluss</div>
      <div class="photo photo--hands" role="img" aria-label="Foto: Hände halten ein rotes Herz"></div>
    </div>
    <h2 class="cover-sub">MIT HERZ AN IHRER SEITE</h2>
    <p class="tagline">Entlastung für Angehörige – Lebensqualität für Senioren</p>
    <div class="gallery">
      <div class="photo photo--scene" role="img" aria-label="Foto: Alltagsbegleiterin liest mit einer Seniorin"></div>
      <div class="photo photo--scene" role="img" aria-label="Foto: Alltagsbegleiterin im Gespräch mit einer Seniorin"></div>
    </div>
    <div class="body-copy">
      <p>Manchmal braucht es nur eine<br>helfende Hand, ein offenes Ohr oder gemeinsame Momente, um den Alltag leichter und schöner zu gestalten.</p>
      <p>Als anerkannte Fachkraft nach §§ 45b SGB XI biete ich,<br>Lena Vogt,<br>Ihnen und Ihren Liebsten genau diese Unterstützung<br>– mit viel Empathie und Professionalität.</p>
    </div>
    <div class="cta">
      <div class="label">UNVERBINDLICH ANFRAGERN</div>
      <div class="phone"><svg viewBox="0 0 24 24"><path d="M6.6 10.8a15.1 15.1 0 0 0 6.6 6.6l2.2-2.2a1 1 0 0 1 1-.25 11.4 11.4 0 0 0 3.6.57 1 1 0 0 1 1 1V20a1 1 0 0 1-1 1A17 17 0 0 1 3 4a1 1 0 0 1 1-1h3.5a1 1 0 0 1 1 1c0 1.25.2 2.45.57 3.6a1 1 0 0 1-.25 1z" fill="#fff"/></svg>0123 456 789 00</div>
    </div>
    <p class="note">Leistungen über die Entlastungsleistungen<br>können direkt mit Ihrer Pflegekasse abgerechnet werden!</p>
  </article>
</body>
</html>
```